M Zyvantics Buisness Cards

I need a technology focused clean business card for my employees. I have attached out logo to include in the mocks. We're a modern tech consulting firm that drives to interface humanity with technology in a truly cohesive fashion.

```html
<!DOCTYPE html>
<html lang="en">
<head>
<meta charset="utf-8">
<title>M Zyvantics Business Cards</title>
<link href="https://fonts.googleapis.com/css2?family=Exo+2:wght@500;600&family=Roboto:wght@400&display=swap" rel="stylesheet">
<style>
  :root {
    --backdrop: #2b2b2d;
    --card: #201c22;
    --brand-blue: #2f7fc6;
    --brand-grey: #8a8b8e;
    --text-light: #b7b8bb;
    --shadow: rgba(0,0,0,0.55);
  }
  * { margin: 0; padding: 0; box-sizing: border-box; }
  html, body { width: 1200px; height: 900px; overflow: hidden; background: var(--backdrop); }
  .stage { position: relative; width: 1200px; height: 900px; }
  .card {
    position: absolute; top: 301px; width: 515px; height: 296px;
    background: var(--card); box-shadow: 0 6px 18px var(--shadow); overflow: hidden;
  }
  .card--front { left: 73px; }
  .card--back { left: 615px; }

  .wordmark { display: flex; align-items: center; gap: 12px;
    font-family: "Exo 2", sans-serif; font-weight: 600; color: var(--brand-grey);
    letter-spacing: 0.04em; white-space: nowrap; }
  .wordmark__dot { width: 14px; height: 14px; border-radius: 50%; background: var(--brand-blue); }
  .card--front .wordmark { position: absolute; left: 0; right: 0; top: 128px; justify-content: center; font-size: 38px; }
  .card--back .wordmark { position: absolute; right: 33px; top: 56px; font-size: 34px; }

  .person { position: absolute; left: 34px; top: 166px; font-family: "Exo 2", sans-serif; }
  .person__name { color: var(--brand-blue); font-size: 16px; font-weight: 600; letter-spacing: 0.08em; }
  .person__role { color: var(--text-light); font-size: 12px; font-weight: 500; letter-spacing: 0.1em; margin-top: 3px; }

  .contacts { position: absolute; left: 34px; top: 219px; list-style: none;
    font-family: "Roboto", sans-serif; font-size: 13px; color: var(--text-light); }
  .contacts li { display: flex; align-items: center; gap: 6px; height: 17px; white-space: nowrap; }
  .contacts li.contacts__email { font-size: 12px; }
  .contacts svg { width: 11px; height: 11px; flex: none; }

  .address { position: absolute; right: 33px; top: 219px; text-align: right; list-style: none;
    font-family: "Roboto", sans-serif; font-size: 13px; color: var(--text-light); }
  .address li { height: 17px; line-height: 17px; white-space: nowrap; }
</style>
</head>
<body>
<main class="stage">
  <section class="card card--front">
    <div class="wordmark"><span class="wordmark__dot"></span>M ZYVANTICS</div>
  </section>

  <section class="card card--back">
    <div class="wordmark"><span class="wordmark__dot"></span>M ZYVANTICS</div>

    <div class="person">
      <p class="person__name">DANIEL MARROW</p>
      <p class="person__role">MANAGING DIRECTOR</p>
    </div>

    <ul class="contacts">
      <li>
        <svg viewBox="0 0 11 11" aria-hidden="true"><rect x="0.5" y="0.5" width="10" height="10" rx="2.5" fill="none" stroke="#2f7fc6"/><path d="M3 4.2q2.5-1.6 5 0l-.6 1-1-.4v-.6h-1.8v.6l-1 .4z" fill="#2f7fc6"/></svg>
        555 014 27 36
      </li>
      <li>
        <svg viewBox="0 0 11 11" aria-hidden="true"><rect x="0.5" y="0.5" width="10" height="10" rx="2.5" fill="none" stroke="#2f7fc6"/><rect x="3.7" y="2.5" width="3.6" height="6" rx="0.8" fill="none" stroke="#2f7fc6" stroke-width="0.9"/></svg>
        888 203 61 49
      </li>
      <li class="contacts__email">
        <svg viewBox="0 0 11 11" aria-hidden="true"><rect x="0.5" y="0.5" width="10" height="10" rx="2.5" fill="none" stroke="#2f7fc6"/><rect x="2.6" y="3.5" width="5.8" height="4" fill="#2f7fc6"/></svg>
        d.marrow@mzyvantics.com
      </li>
    </ul>

    <ul class="address">
      <li>48 Harlow Lane</li>
      <li>Brookvale, Westbrook 40817</li>
      <li>www.mzyvantics.com</li>
    </ul>
  </section>
</main>
</body>
</html>
```